Nutritional & Gastrointestinal Health Consulting Service-Website design

We need a website design for a new health consulting service called "Bright Harbor" based in Perth, Australia.

We will be providing consulting services in the areas of:
1) Nutrition and Diet
2) Gastrointestinal Health (which means stomach & digestive system related health)

These consulting services will be provided by an Accredited Dietitian and a Paediatric Gastroenterologist.

We are open to creative ideas in terms of design, layout, fonts and colours. We also would love to see images of nature in the backdrop with families (adults with kids) having a good time, fresh fruits and vegetables displayed in a farmer's market or supermarket. 2 or 3 images should be sufficient. We would also definitely want our logo somewhere in the main page of website. The logo file is also attached. Please have a look at a website's design that we really liked. We would love to see designs inspired by that style. The website details are in the in the "nice to have priorities" section of this project brief.

We also would be looking at website designers with software coding skills so that if we like the design we can go ahead with the next step of coding.

The website design should communicate the purpose of the website and at the same time be simple, elegant and unique/eye-catching.

We look forward to receiving creative ideas for our website from you all. Good luck!
Updates

More details have been added to our project- for example: Logo, fonts style, must haves etc etc. Please view the updated project brief. Looking forward to receiving your fantastic ideas for our website. Thanking you

Hi, I have updated the colour preference. Will add the content preferences tomorrow. thanks

Hello all, I have now added a LOT more content to what we want in our website. It is very much in detail, so please carefully have a read through the entire project brief. If you have any questions write back to me and I will try to respond as quickly as I can. Last few days were busy so couldn't respond quickly to all of you who had send me designs/queries/questions. Thank you for your patience. I look forward to receiving fantastic designs from you all. Good Luck :-)

Target Market(s)

Adults based in western speaking countries aged 18 to 60 years

Industry/Entity Type

Software

Font styles to use
Sans Serif
Script

Colors
faa54b
acd036

Requirements
Must have
• The website must have the MAIN logo file attached. I have attached 3 files: 1) MAIN logo; 2) supplementary logo A ; 3) supplementary logo B

I have selected 2 colours from the colour scheme (see below)-(as the colour of our logo is that).
However we would also like to see LIGHT CHOCOLATE BROWN or CHOCOLATE BROWN colour used as the background colour of the website
Preferred WEBSITE CONTENT:
1) HOME PAGE:
Content required=
--Company Logo
--Dr Ravel Ostrin
Paediatric Gastroenterologist & Hepatologist
-Leora Ostrin.
Dietitian & Nutritionist
--Website Menu (either listed horizontally or vertically):
Once clicked on each name:

Under each of the Website Menu items we want the following Headings to be added

2) ABOUT US page:
Sub-heading under this: Qualification, Skills, Special Interest

3) SERVICES
RAVEL'S PAGE: Individual Consultation, Endoscopy procedures
Individual Consultation, Group Based Services, Food Diary, Food & Symptom Diary

4) FEES & REBATE: Content as below:
Please Note: Payment of full fees is required at the time of consultation and procedures. 48 hours notice is required for cancellation of appointments/non-attendance. Failure to provide this may result in a fee being incurred. Please call reception to find out the amount of fee charged for cancellation of appointments/non-attendance.
headings are:
Paediatric Gastroenterology:
Ravel's pge
Individual Consultation - Initial (upto 30 mins):
Review Consultation (upto 15 mins):
Endoscopy procedures - No Gap fees charged. Fees will be billed directly to Carewell. If any queries, please contact reception.

leora's pge
sub heading:
Individual Consultation - Initial (upto 45 mins):
Individual Consultation - Review (upto 30 mins):

Concession-Individual Consultation -Initial (upto 45 mins):
Concession-Individual Consultation - Review (upto 30 mins):
Please Note: Concession applies for health care card holders & pensioners

Group Based Services: Pricing subject to the type of service provided. Please contact us for an obligation free quote.
Education Topics Include:
- Paediatric Nutrition (Introducing Solids, Fussy Eating, Healthy Eating)
- Pregnancy Nutrition, Gestational Diabetes, Breastfeeding/Lactation Nutrition
- Healthy Eating, Supermarket Shopping Tips, Nutrition Label Reading Tips, Healthier
sub heading under nutrition & diet:
-Carewell:
--A rebate of $52.95 is available from Carewell if an EPC ( Enhanced Primary Care)/Chronic Disease Management (CDM) plan is issued by your GP.
--All mandatory paperwork needs to be available at the time of making your appointment for your eligibility.
-Private Health Fund:
--Most private health funds provide rebate on dietetic appointments. However the rebate amount depends on your level of cover. Thus, please contact your health fund to determine your entitled rebate.
-KRB: Approved provider for KRB services

6) FOR DOCTORS: Bright Harbor Paediatric Gastroenterologist Referral Form
Bright Harbor Dietitian Referral form
7) LOCATIONS & CONTACT

Paediatric Gastroenterology & Hepatology Service
Suite 82
Holloway Brenton Medical Centre
17 Quillan Fenwick Pde,
GLENDRA, WA 6177
P: (08) 9472 5031
F: (08) 9472 6640

Nutrition & Diet Service
Suite 82
17 Quillan Fenwick Pde,
GLENDRA, WA 6177
P: (08) 9472 5031
F: (08) 9472 6640

Tolliver Medical Centre
58-60 Corvane Parkway,
PELLARD, WA 6238
P: (08) 9627 4083
F: (08) 96274092
www.tmcpellard.com.au

This page should have a webform that has following titles:
-Your Name
-Your Email
-Your Phone
-Message

8) NEWS & BLOG
Nice to have
• We liked the design style of the websites below:
https://www.vivoraclinic.example/

http://tummywise.example/

But feel free to use your creativity too
Should not have
• Please do not use any body building or muscle building images

```html
<!DOCTYPE html>
<html lang="en">
<head>
<meta charset="utf-8">
<title>Bright Harbor – Paediatric Gastroenterology &amp; Nutrition</title>
<link href="https://fonts.googleapis.com/css2?family=Hind:wght@400;500;600;700&display=swap" rel="stylesheet">
<style>
  :root {
    --pan-dark: #23240c;
    --pan-edge: #3a3a14;
    --food-brown: #6e4a22;
    --food-warm: #8a5e2a;
    --food-red: #7a3a1c;
    --leaf-green: #5e7a1e;
    --table-light: #8f9c3c;
    --corner-light: #a3ad4e;
    --hero-tint: rgba(110, 140, 20, 0.22);
    --white: #ffffff;
    --accent-orange: #faa54b;
    --accent-green: #acd036;
    --footer-bg: #ffffff;
    --footer-line: #ececec;
    --footer-active: #eef5fb;
    --ink: #1d1d1d;
  }
  * { margin: 0; padding: 0; box-sizing: border-box; }
  html, body {
    width: 1200px; height: 645px; overflow: hidden;
    font-family: "Hind", Arial, sans-serif;
    background: var(--footer-bg);
  }
  .hero {
    position: relative; width: 1200px; height: 593px; overflow: hidden;
  }
  .hero-photo {
    position: absolute; inset: 0;
    background:
      radial-gradient(ellipse 260px 160px at 560px 300px, var(--food-warm) 0%, transparent 75%),
      radial-gradient(ellipse 180px 120px at 380px 380px, var(--food-red) 0%, transparent 75%),
      radial-gradient(ellipse 200px 140px at 760px 390px, var(--food-brown) 0%, transparent 75%),
      radial-gradient(ellipse 160px 90px at 520px 150px, var(--leaf-green) 0%, transparent 75%),
      radial-gradient(ellipse 470px 300px at 590px 300px, var(--food-brown) 0%, var(--pan-edge) 82%, transparent 100%),
      radial-gradient(ellipse 620px 400px at 560px 290px, var(--pan-dark) 60%, transparent 100%),
      radial-gradient(ellipse 260px 260px at 1150px 560px, var(--table-light) 0%, transparent 80%),
      radial-gradient(ellipse 220px 240px at 0px 0px, var(--corner-light) 0%, transparent 80%),
      radial-gradient(ellipse 240px 200px at 1180px 40px, var(--pan-dark) 0%, transparent 80%),
      linear-gradient(160deg, #7b8a2e 0%, #4a5418 50%, #6f7e2c 100%);
  }
  .hero-photo::after {
    content: ""; position: absolute; inset: 0; background: var(--hero-tint);
  }
  .brand {
    position: absolute; left: 166px; top: 44px; width: 92px;
    display: flex; flex-direction: column; align-items: center;
  }
  .brand-mark {
    width: 46px; height: 46px; border-radius: 50%;
    background: var(--accent-orange); margin-bottom: 8px;
  }
  .brand-name {
    font-weight: 700; font-size: 17px; line-height: 17px;
    color: var(--accent-green); text-align: center; letter-spacing: 0.5px;
  }
  .main-nav {
    position: absolute; top: 86px; right: 156px;
    display: flex; gap: 23px;
  }
  .main-nav a {
    color: var(--white); text-decoration: none;
    font-weight: 600; font-size: 11.5px; line-height: 16px;
    position: relative;
  }
  .main-nav a.is-active::after {
    content: ""; position: absolute; left: 0; right: 0; bottom: -5px;
    height: 2px; background: var(--accent-orange);
  }
  .hero-copy {
    position: absolute; left: 0; right: 0; top: 240px; text-align: center;
    color: var(--white);
  }
  .hero-copy h1 {
    font-weight: 600; font-size: 37px; line-height: 45px;
    text-shadow: 0 1px 4px rgba(0,0,0,0.45);
  }
  .hero-copy p {
    margin-top: 39px; font-size: 19px; line-height: 22px; font-weight: 400;
    text-shadow: 0 1px 3px rgba(0,0,0,0.4);
  }
  .site-footer {
    position: relative; height: 52px; background: var(--footer-bg);
  }
  .social-links {
    position: absolute; left: 166px; top: 0; display: flex;
    border-left: 1px solid var(--footer-line);
  }
  .social-links a {
    width: 48px; height: 52px; border-right: 1px solid var(--footer-line);
    display: flex; align-items: center; justify-content: center;
  }
  .social-links a.is-active { background: var(--footer-active); }
  .social-links span { width: 10px; height: 10px; display: block; }
  .dot-sky { background: #2aa9e0; border-radius: 50%; }
  .dot-navy { background: #1c3f94; }
  .dot-red { background: #d9412f; }
  .copyright {
    position: absolute; right: 156px; top: 20px;
    font-size: 11px; font-weight: 600; color: var(--ink);
  }
</style>
</head>
<body>
  <header class="hero">
    <div class="hero-photo" role="img" aria-label="Close-up of a cast iron pan with stir-fried meat, red chilli and spring onions under a green tint"></div>
    <div class="brand">
      <span class="brand-mark"></span>
      <span class="brand-name">BRIGHT<br>HARBOR</span>
    </div>
    <nav class="main-nav">
      <a href="#">About Us</a>
      <a href="#" class="is-active">Nutrition &amp; Diet</a>
      <a href="#">Paediatric Gastroenterology &amp; Hepatology</a>
      <a href="#">Fees &amp; Rebate</a>
      <a href="#">For Doctors</a>
      <a href="#">News &amp; Blog</a>
      <a href="#">Contact</a>
    </nav>
    <div class="hero-copy">
      <h1>Welcome to a comprehensive paediatric<br>gastroenterology &amp; hepatology service.</h1>
      <p>Bright Harbor team includes a Paediatric Gastroenterologist &amp; Hepatologist -Dr Ravel Ostrin and an<br>Accredited Dietitian-Leora Ostrin.</p>
    </div>
  </header>
  <footer class="site-footer">
    <div class="social-links">
      <a href="#" aria-label="Social link"><span class="dot-sky"></span></a>
      <a href="#" class="is-active" aria-label="Social link"><span class="dot-navy"></span></a>
      <a href="#" aria-label="Social link"><span class="dot-red"></span></a>
    </div>
    <p class="copyright">© Bright Harbor Company</p>
  </footer>
</body>
</html>
```